Bref créative
Book Cover
The Steelheart’s Manual to Illness Endurance
PRESS RELEASE
For immediate release:
Cancer Survivor Tom Brelsky Announces Release of ‘The Steelheart’s Manual to Illness Endurance’
For Tom Brelsky, it all started with a heartwarming story, and became an accomplishment that had never before been achieved.
WASHINGTON, DC —The first Steelheart triathlete to have ever completed the event following a bone marrow transplant for CML (Chronic Myelogenous Leukemia) from an unrelated donor, announces that his new book ‘The Steelheart’s Manual to Illness Endurance’ is scheduled for release later this summer. Brelsky has taken cancer survival to new heights not just through his athletic achievements, but also through his work to help other cancer survivors via his extraordinary fundraising and website, www.qbvr-example.org.
Brelsky’s defiance of the odds, by his own admission, has led him to a higher purpose in his life, and this announcement only certifies his commitment to getting his unique and powerful message out to as many people as possible, be they cancer survivors themselves, friends or family members of survivors, fellow athletes, or those who just want to be inspired.
Tom’s Incredible Story
Tom Brelsky was a young, twenty-seven year-old architect when he was diagnosed with CML in 1998. At the time, the only reliable treatment was to undergo a rigorous bone marrow transplant, which required that his entire blood and immune system be destroyed, and then replaced with that from a donor. The procedure is known as one of the most difficult medical procedures to withstand and Brelsky spent months in the hospital and over a full year before returning to work.
Brelsky’s body accepted the transplant and he was on his way to a full recovery, but something in his life seemed incomplete. After becoming involved with a support and endurance athlete training group organized through the Marrow and Plasma Alliance, he began to raise money for the MPA and train to run marathons. He eventually set his sights on the Steelheart triathlon, a 140.6 mile event that includes a long swim (2.4 miles), a longer bike ride (112 miles) and then capped by full marathon (26.2 miles). Brelsky successfully completed his first Steelheart in 2008 to celebrate the ten-year anniversary of his bone marrow transplant. Through the numerous events in which he has competed, he has raised more than $240,000 to support blood cancer research.
Contents and Release Dates for ‘The Steelheart’s Manual to Illness Endurance’
The ‘Steelheart’s Manual to Illness Endurance’ has three distinct components. First, a reader will walk through Tom’s story, from his life before cancer, to the diagnosis and treatment, and to the subsequent training that led him to completing not one, but two Steelheart triathlons! Next, there are dozens of tips that are as pertinent for the cancer survivor as they are for someone simply wanting to lead a healthier and more productive life. Each set of tips in this section is linked to one of the legs of an Steelheart triathlon, putting readers literally in Tom’s shoes as they take this journey toward better personal wellness. Last, a reader will find a compelling discussion of giving back, and how to seize the day by setting powerful, action-based goals for personal success.
Having discovered a new life purpose as a cancer survivor, Tom Brelsky is a recognized leader in raising funds and awareness of how better to survive cancer. His upcoming book release, ‘The Steelheart’s Manual to Illness Endurance’, can be preordered through his website www.qbvr-example.org, later this summer. His accomplishments are unparalleled but his mission is simple, to help as many fellow cancer survivors and the people whose lives are impacted by this disease, as he possibly can.
For more information on the ‘The Steelheart’s Manual to Illness Endurance’ book release:
http://www.firstdawntosteelheart-example.org
The book cover needs to be similiar to the website. Please use the website design to influence the design. I like the blood cells.
The book cover is 6" by 9"
Must look at www.qbvr-example.org to inspiration
The picture of me should be on the cover.
My logo should be on the book cover somewhere...

```html
<!DOCTYPE html>
<html lang="en">
<head>
<meta charset="utf-8">
<title>The Steelheart’s Manual to Illness Endurance — Book Cover</title>
<link href="https://fonts.googleapis.com/css2?family=Tinos:ital,wght@0,400;0,700;1,700&family=Arimo:wght@400;700&display=swap" rel="stylesheet">
<style>
  :root {
    --paper: #ffffff;
    --ink: #1a1a1a;
    --accent-red: #c0272d;
    --accent-orange: #f26a1b;
    --night: #0b0d10;
    --photo-top: #3a4a55;
    --photo-low: #14181c;
    --cell-red: #9a1418;
    --cell-dark: #2a0608;
  }
  * { margin: 0; padding: 0; box-sizing: border-box; }
  html, body { width: 1200px; height: 859px; overflow: hidden; background: #ffffff; }
  .cover-spread { position: relative; width: 1200px; height: 859px; display: flex; }

  /* Back cover */
  .back-cover {
    width: 567px; height: 859px; background: var(--paper);
    padding: 16px 16px 0 10px; position: relative;
    font-family: "Tinos", "Times New Roman", serif; color: var(--ink);
  }
  .back-heading {
    font-weight: 400; font-size: 16px; line-height: 18px;
    color: var(--accent-red); margin-bottom: 2px;
  }
  .back-body p {
    font-size: 13.6px; line-height: 15.6px; text-align: justify;
    text-indent: 22px;
  }
  .back-body p.section-title { text-align: center; text-indent: 0; }
  .imprint {
    position: absolute; left: 10px; bottom: 16px;
    font-family: "Tinos", "Times New Roman", serif; font-weight: 400;
    font-size: 12px; line-height: 14px; color: var(--ink);
  }

  /* Spine */
  .spine {
    width: 62px; height: 859px; background: var(--paper); position: relative;
    border-left: 1px solid #e6e6e6; border-right: 1px solid #e6e6e6;
  }
  .spine-title {
    position: absolute; top: 12px; left: 50%;
    transform-origin: 0 0; transform: rotate(90deg) translateY(-50%);
    white-space: nowrap; font-family: "Arimo", Arial, sans-serif;
    color: var(--accent-orange); font-size: 30px; line-height: 40px;
  }
  .spine-title strong { font-weight: 700; font-size: 34px; letter-spacing: 0.5px; }
  .spine-imprint {
    position: absolute; bottom: 16px; left: 0; width: 100%;
    text-align: center; font-family: "Tinos", "Times New Roman", serif;
    font-size: 9px; line-height: 11px; color: var(--ink);
  }

  /* Front cover */
  .front-cover {
    flex: 1; height: 859px; position: relative; overflow: hidden;
    background: var(--night);
  }
  .author-photo {
    position: absolute; left: 0; top: 0; width: 100%; height: 560px;
    background: radial-gradient(ellipse at 62% 30%, #5f7480 0%, var(--photo-top) 35%, var(--photo-low) 80%, var(--night) 100%);
  }
  .blood-cells {
    position: absolute; left: 0; bottom: 0; width: 100%; height: 200px;
    background: radial-gradient(ellipse at 50% 95%, var(--cell-red) 0%, var(--cell-dark) 55%, var(--night) 100%);
  }
  .front-title {
    position: absolute; left: 22px; top: 560px; font-weight: 400;
    font-family: "Arimo", Arial, sans-serif; color: var(--paper);
  }
  .front-title .title-lead { display: block; font-size: 33px; line-height: 40px; }
  .front-title .title-main {
    display: block; font-weight: 700; font-size: 47px; line-height: 56px;
    color: var(--accent-orange); letter-spacing: 0.5px;
  }
  .front-author {
    position: absolute; left: 150px; top: 702px; white-space: nowrap;
    font-family: "Arimo", Arial, sans-serif; font-size: 21px; color: var(--accent-orange);
  }
  .front-author::after {
    content: ""; display: inline-block; width: 260px; margin-left: 6px;
    vertical-align: middle; border-top: 1px solid var(--accent-orange);
  }
</style>
</head>
<body>
<main class="cover-spread">
  <section class="back-cover">
    <h2 class="back-heading">Tom’s Incredible Story</h2>
    <div class="back-body">
      <p>Tom Brelsky was a young, twenty-seven year-old architect when he was diagnosed with CML in 1998. At the time, the only reliable treatment was to undergo a rigorous bone marrow transplant, which required that his entire blood and immune system be destroyed, and then replaced with that from a donor. The procedure is known as one of the most difficult medical procedures to withstand and Brelsky spent months in the hospital and over a full year before returning to work.</p>
      <p>Brelsky’s body accepted the transplant and he was on his way to a full recovery, but something in his life seemed incomplete. After becoming involved with a support and endurance athlete training group organized through the Marrow and Plasma Alliance, he began to raise money for the MPA and train to run marathons. He eventually set his sights on the Steelheart triathlon, a 140.6 mile event that includes a long swim (2.4 miles), a longer bike ride (112 miles) and then capped by full marathon (26.2 miles). Brelsky successfully completed his first Steelheart in 2008 to celebrate the ten-year anniversary of his bone marrow transplant. Through the numerous events in which he has competed, he has raised more than $240,000 to support blood cancer research.</p>
      <p class="section-title">Contents and Release Dates for ‘The Steelheart’s Manual to Illness Endurance’</p>
      <p>The ‘Steelheart’s Manual to Illness Endurance’ has three distinct components. First, a reader will walk through Tom’s story, from his life before cancer, to the diagnosis and treatment, and to the subsequent training that led him to completing not one, but two Steelheart triathlons! Next, there are dozens of tips that are as pertinent for the cancer survivor as they are for someone simply wanting to lead a healthier and more productive life. Each set of tips in this section is linked to one of the legs of an Steelheart triathlon, putting readers literally in Tom’s shoes as they take this journey toward better personal wellness. Last, a reader will find a compelling discussion of giving back, and how to seize the day by setting powerful, action-based goals for personal success.</p>
      <p>Having discovered a new life purpose as a cancer survivor, Tom Brelsky is a recognized leader in raising funds and awareness of how better to survive cancer. His upcoming book release, ‘The Steelheart’s Manual to Illness Endurance’, can be preordered through his website www.qbvr-example.org, later this summer. His accomplishments are unparalleled but his mission is simple, to help as many fellow cancer survivors and the people whose lives are impacted by this disease, as he possibly can.</p>
    </div>
    <div class="imprint">Kestrel Bay Press</div>
  </section>

  <section class="spine">
    <div class="spine-title">The Steelheart’s Manual to <strong>ILLNESS ENDURANCE</strong></div>
    <div class="spine-imprint">Kestrel<br>Bay Press</div>
  </section>

  <section class="front-cover">
    <div class="author-photo" role="img" aria-label="Photograph of the author in swim cap and goggles, wearing a wetsuit, against a dark background"></div>
    <div class="blood-cells" role="img" aria-label="Illustration of red blood cells glowing in a dark red stream"></div>
    <h1 class="front-title">
      <span class="title-lead">The Steelheart’s Manual to</span>
      <span class="title-main">ILLNESS ENDURANCE</span>
    </h1>
    <p class="front-author">By Tom Brelsky</p>
  </section>
</main>
</body>
</html>
```